Commercial Rooftop Solar business needs a website

We need a website with fantastic appeal for a new company based in Melbourne called Tidewell Energy. We design and install solar energy systems for commercial applications across Australia. Our market is to focus on small to medium businesses looking for solar solutions, but we will also provide our service for residential customers. We would like a beautiful 'front page' feel to our home page, using photographs of solar PV systems and/or natural imagery. Our logo uses the colours orange and black, which could easily be echoed in photographic imagery of sunset and sunrise, for example. The design should communicate quiet confidence and professionalism to a corporate marketplace.

NEW POINTS FOR BRIEF: This design also needs to be flexible to allow for additional future content, including a Support page with sub pages, FAQ's, and a Blog.

As part of this design project, we will require the coding for the website to be completed by the designer.

We have seen some websites, which we like the look and feel of: these are listed below.

brightquarrypower.com.au:

• Beautiful images underlaying brief text selling points.
• Simple ‘front cover’ style home page with elegant drop-down menu, stylish simple font style.
• Home page invites exploration through the menu links, rather than trying to provide all the information up front.
• Company logo and name in the top left hand corner, contact details accessible at top right hand, seems consistent in most sites.

fonvaleenergy.com.au

murlockenergy.com:
• Same element as the others is the front-page style home page with beautiful images underlying text.

We have a webpage that we started uploading content to. You can use some of the content there in your designs: www.tidewellenergy.com.au

Technical Specifications:
PAGES:

Home

About Us

Solutions - Commercial
- Residential

Products - Solar Panels - Vorla Kestrel, Vorla TUSK, Vorla QB
- Solar Inverters - Delmark, VoltHaven
- Monitoring systems - Grid Insight
- Batteries - KD

- Datasheets have been provided for reference but if it's too much work, you can use generic text and we will provide content later.

Contact Us

FUTURE PAGES (Please consider in structure, where links could be placed):

Support

FAQ's

Blog.

We could provide some content for the Support page soon, but the Blog and FAQ's are future pages which we don't want highlighted in the design as we don't yet have content.

Phone: 1800 7 TIDEW
Email: sales@tidewellenergy.com.au

Currently, I do not have images and text available. Please
use placeholders in the meantime. The final text and images will be uploaded for the winner once a winning design has been selected.

Target Market(s)

Primary focus is on small to medium sized business owners. Those owners will have a house which may be suitable for solar so we want to cater to residential deeper in the website.

Industry/Entity Type

Solar Energy

Coding

Coded - Design and coding required

Number of Pages Required

5+ page

Colors
f78f20
0255a3

Requirements
Must have
• Logo as per attachments.
Nice to have
• Logo can have alternate colours Eg. White on Orange or Black etc. provided colour correct logo is shown somewhere eg. footer or contact page.
• In the active site, I'd like to have:
• Very slowly zooming images - barely perceptible.
• Title text that rolls into place
• Subtle movements
• See https://pellbrook.com.au/ for example

```html
<!DOCTYPE html>
<html lang="en">
<head>
<meta charset="utf-8">
<title>Tidewell Energy</title>
<link href="https://fonts.googleapis.com/css2?family=Poppins:wght@500;600;700&family=Lato:wght@400;700&family=Questrial&display=swap" rel="stylesheet">
<style>
:root{
  --blue:#0255a3;
  --orange:#f78f20;
  --ink:#222;
  --body:#555;
  --grey-band:#ececec;
  --card-border:#ececec;
  --white:#fff;
}
*{box-sizing:border-box;margin:0;padding:0}
html,body{width:1200px;height:2479px;overflow:hidden;background:var(--white)}
body{position:relative;font-family:'Questrial',sans-serif;color:var(--body)}
.abs{position:absolute}

/* header */
.site-header{position:absolute;left:0;top:0;width:1200px;height:109px;background:var(--white)}
.nav-panel{position:absolute;left:0;top:0}
.brand{position:absolute;left:132px;top:34px;display:flex;align-items:center;gap:14px}
.brand-dot{width:40px;height:40px;border-radius:50%;background:var(--orange)}
.brand-name{font-family:'Poppins',sans-serif;font-weight:600;font-size:26px;color:#1d1d1d;letter-spacing:.5px}
.main-nav{position:absolute;top:38px;left:0;font-family:'Poppins',sans-serif;font-weight:600;font-size:21px;color:var(--white)}
.main-nav span{position:absolute;white-space:nowrap}

/* hero */
.hero{position:absolute;left:0;top:109px;width:1200px;height:506px;
  background:linear-gradient(180deg,#3d4f66 0%,#26354a 45%,#1b2736 80%,#2f3a22 100%)}
.bracket{position:absolute;width:46px;height:46px;border-color:var(--white);border-style:solid;border-width:0}
.b-tl{left:248px;top:84px;border-top-width:2px;border-left-width:2px}
.b-tr{left:908px;top:84px;border-top-width:2px;border-right-width:2px}
.b-bl{left:248px;top:374px;border-bottom-width:2px;border-left-width:2px}
.b-br{left:908px;top:374px;border-bottom-width:2px;border-right-width:2px}
.hero-kicker{position:absolute;top:112px;width:1200px;text-align:center;font-family:'Poppins',sans-serif;font-weight:600;font-size:25px;color:var(--white)}
.hero-title{position:absolute;top:145px;width:1200px;text-align:center;font-family:'Poppins',sans-serif;font-weight:600;font-size:50px;color:var(--orange);letter-spacing:.5px}
.hero-text{position:absolute;left:270px;top:222px;width:660px;text-align:center;font-family:'Poppins',sans-serif;font-weight:500;font-size:14.5px;line-height:32px;color:var(--white)}
.btn{position:absolute;background:var(--blue);color:var(--white);font-family:'Poppins',sans-serif;font-weight:600;font-size:15px;display:flex;align-items:center;justify-content:center}
.hero .btn{left:512px;top:347px;width:148px;height:40px;font-size:16px}

/* section titles */
.section-title{position:absolute;width:1200px;text-align:center;font-family:'Lato',sans-serif;font-weight:700;font-size:32px;color:var(--blue)}
.zigzag{position:absolute}

/* offer cards */
.offer-card{position:absolute;top:777px;width:296px;height:344px;background:var(--white);box-shadow:0 0 8px rgba(0,0,0,.08)}
.corner{position:absolute;width:30px;height:30px;border:0 solid var(--orange)}
.corner-tl{left:23px;top:23px;border-top-width:1.5px;border-left-width:1.5px}
.corner-br{right:23px;bottom:23px;border-bottom-width:1.5px;border-right-width:1.5px}
.offer-icon{position:absolute;left:118px;top:62px}
.offer-name{position:absolute;top:126px;width:100%;text-align:center;font-family:'Lato',sans-serif;font-weight:700;font-size:20px;color:var(--orange);letter-spacing:.5px}
.offer-text{position:absolute;left:22px;top:170px;width:252px;text-align:center;font-family:'Lato',sans-serif;font-weight:700;font-size:11.5px;line-height:21.5px;color:#777}
.offer-card .btn{left:86px;top:251px;width:124px;height:38px}

/* about */
.about-band{position:absolute;left:0;top:1187px;width:1200px;height:433px;background:var(--grey-band)}
.about-photo{position:absolute;left:132px;top:1256px;width:339px;height:298px;border:3px solid var(--orange);
  background:linear-gradient(180deg,#aeb9c4 0%,#cdd3d8 45%,#3e4656 62%,#8b9096 78%,#b9bcbe 100%)}
.about-title{position:absolute;left:496px;top:1244px;font-family:'Lato',sans-serif;font-weight:700;font-size:33px;color:var(--blue)}
.about-text{position:absolute;left:496px;width:562px;font-family:'Lato',sans-serif;font-size:11.6px;line-height:17.5px;color:#666}
.about-btn{left:496px;top:1516px;width:124px;height:39px}

/* testimonials */
.quote-card{position:absolute;top:1777px;width:286px;height:317px;background:var(--white);border:1px solid var(--card-border);border-bottom:3px solid var(--orange)}
.avatar{position:absolute;left:111px;top:23px;width:63px;height:63px;border-radius:50%;background:linear-gradient(160deg,#d9dde2,#6d7480)}
.quote-text{position:absolute;left:22px;top:116px;width:242px;text-align:center;font-size:12px;line-height:22px;color:#444}
.quote-rule{position:absolute;left:48px;top:232px;width:190px;height:1px;background:#e6e6e6}
.quote-name{position:absolute;top:255px;width:100%;text-align:center;font-family:'Poppins',sans-serif;font-weight:600;font-size:13px;color:#333}
.quote-company{position:absolute;top:276px;width:100%;text-align:center;font-size:10px;color:#999}
.dots{position:absolute;left:582px;top:2127px;display:flex;gap:6px}
.dots i{width:9px;height:9px;border-radius:50%;background:#d8d8d8;display:block}
.dots i.active{background:var(--orange)}

/* footer */
.site-footer{position:absolute;left:0;top:2202px;width:1200px;height:277px;background:var(--blue);color:var(--white)}
.footer-brand{position:absolute;left:149px;top:46px;display:flex;align-items:center;gap:14px}
.footer-brand .brand-dot{background:var(--white);width:38px;height:38px}
.footer-brand .brand-name{color:var(--white);font-size:25px}
.footer-about{position:absolute;left:149px;top:112px;width:385px;font-size:11.6px;line-height:18.5px}
.footer-head{position:absolute;top:56px;font-family:'Lato',sans-serif;font-weight:700;font-size:15px}
.footer-links{position:absolute;left:597px;top:110px;width:196px;list-style:none;font-size:12px}
.footer-links li{height:30px;line-height:26px;border-bottom:1px solid rgba(255,255,255,.18);padding-left:18px;position:relative}
.footer-links li:last-child{border-bottom:0}
.footer-links li::before{content:"";position:absolute;left:3px;top:11px;width:5px;height:5px;border-radius:50%;background:var(--white)}
.contact-row{position:absolute;left:861px;font-size:12px;line-height:19px;display:flex;gap:10px}
.contact-row svg{flex:none;margin-top:3px}
</style>
</head>
<body>

<header class="site-header">
  <svg class="nav-panel" width="1200" height="109"><polygon points="488,0 1124,0 1200,109 410,109" fill="#0255a3"/></svg>
  <div class="brand"><span class="brand-dot"></span><span class="brand-name">Tidewell Energy</span></div>
  <nav class="main-nav">
    <span style="left:529px">HOME</span>
    <span style="left:612px">SOLUTIONS</span>
    <span style="left:745px">PRODUCTS</span>
    <span style="left:876px">ABOUT</span>
    <span style="left:969px">CONTACT</span>
  </nav>
</header>

<section class="hero" role="img" aria-label="Photograph of solar panel rows with wind turbines under a cloudy sky">
  <span class="bracket b-tl"></span><span class="bracket b-tr"></span>
  <span class="bracket b-bl"></span><span class="bracket b-br"></span>
  <h2 class="hero-kicker">WELCOME TO</h2>
  <h1 class="hero-title">TIDEWELL ENERGY</h1>
  <p class="hero-text">Tidewell Energy is a national company that specialises in solar solutions for the commercial market. We also provide solutions for the residential market, bringing our uncompromising quality and service to the home.</p>
  <a class="btn">Read more</a>
</section>

<h2 class="section-title" style="top:673px">What we offer</h2>
<svg class="zigzag" style="left:470px;top:719px" width="76" height="12"><polyline points="0,6 4,2 8,9 12,2 16,9 20,6 76,6" fill="none" stroke="#f78f20" stroke-width="1.6"/></svg>

<article class="offer-card" style="left:132px">
  <span class="corner corner-tl"></span><span class="corner corner-br"></span>
  <svg class="offer-icon" width="60" height="44" viewBox="0 0 60 44" fill="none" stroke="#0255a3" stroke-width="2">
    <rect x="2" y="2" width="56" height="26"/><line x1="2" y1="11" x2="58" y2="11"/><line x1="2" y1="20" x2="58" y2="20"/>
    <line x1="16" y1="2" x2="16" y2="28"/><line x1="30" y1="2" x2="30" y2="28"/><line x1="44" y1="2" x2="44" y2="28"/>
    <line x1="30" y1="28" x2="30" y2="40"/><line x1="20" y1="41" x2="40" y2="41"/>
  </svg>
  <h3 class="offer-name">VORLASOLAR</h3>
  <p class="offer-text">The Vorla Kestrel Series is the first PID-free module in the world. it's especially ideal for installations in Australia because of its</p>
  <a class="btn">Read more</a>
</article>

<article class="offer-card" style="left:451px">
  <span class="corner corner-tl"></span><span class="corner corner-br"></span>
  <svg class="offer-icon" width="60" height="44" viewBox="0 0 60 44" fill="none" stroke="#0255a3" stroke-width="2">
    <rect x="14" y="14" width="26" height="26"/><line x1="14" y1="23" x2="40" y2="23"/><line x1="14" y1="32" x2="40" y2="32"/>
    <line x1="23" y1="14" x2="23" y2="40"/><line x1="31" y1="14" x2="31" y2="40"/>
    <circle cx="46" cy="8" r="4"/><line x1="46" y1="0" x2="46" y2="2"/><line x1="53" y1="8" x2="56" y2="8"/><line x1="51" y1="3" x2="53" y2="1"/>
    <path d="M18 10c0-3 3-3 3-6M24 10c0-3 3-3 3-6M30 10c0-3 3-3 3-6"/>
  </svg>
  <h3 class="offer-name">GRID INSIGHT</h3>
  <p class="offer-text">The Vorla Kestrel Series is the first PID-free module in the world. it's especially ideal for installations in Australia because of its</p>
  <a class="btn">Read more</a>
</article>

<article class="offer-card" style="left:772px">
  <span class="corner corner-tl"></span><span class="corner corner-br"></span>
  <svg class="offer-icon" width="60" height="44" viewBox="0 0 60 44" fill="none" stroke="#0255a3" stroke-width="2.4">
    <circle cx="20" cy="12" r="5"/><line x1="20" y1="1" x2="20" y2="4"/><line x1="9" y1="12" x2="12" y2="12"/><line x1="12" y1="4" x2="14" y2="6"/><line x1="28" y1="4" x2="26" y2="6"/>
    <polygon points="26,20 48,20 52,36 22,36"/><line x1="37" y1="20" x2="37" y2="36"/><line x1="24" y1="28" x2="50" y2="28"/>
    <line x1="37" y1="36" x2="37" y2="42"/><line x1="30" y1="42" x2="44" y2="42"/>
  </svg>
  <h3 class="offer-name">VOLTHAVEN</h3>
  <p class="offer-text">The Vorla Kestrel Series is the first PID-free module in the world. it's especially ideal for installations in Australia because of its</p>
  <a class="btn">Read more</a>
</article>

<section class="about-band"></section>
<div class="about-photo" role="img" aria-label="Photograph of solar panels on a commercial metal roof under a cloudy sky"></div>
<h2 class="about-title">About us</h2>
<svg class="zigzag" style="left:496px;top:1293px" width="80" height="12"><polyline points="0,6 4,2 8,9 12,2 16,9 20,6 80,6" fill="none" stroke="#f78f20" stroke-width="1.6"/></svg>
<p class="about-text" style="top:1327px">Nam liber tempor cum soluta nobis eleifend option congue nihil imperdiet doming id quod mazim placerat facer possim assum. Lorem ipsum dolor sit amet laaoree, consectetuer adipiscing elit, sed diam nonummy nibh euismod tincidunt.</p>
<p class="about-text" style="top:1404px">Nam liber tempor cum soluta nobis eleifend option congue nihil imperdiet doming id quod mazim placerat facer possim assum. Lorem ipsum dolor sit amet laaoree, consectetuer adipiscing elit, sed diam nonummy nibh euismod tincidunt.Nam liber tempor cum soluta nobis eleifend option congue nihil imperdiet doming id quod mazim placerat facer possim assum. Lorem ipsum dolor sit amet laaoree, consectetuer adipiscing elit, sed diam nonummy nibh euismod tincidunt.</p>
<a class="btn about-btn">Read more</a>

<h2 class="section-title" style="top:1678px">What our clients say</h2>
<svg class="zigzag" style="left:452px;top:1725px" width="80" height="12"><polyline points="0,6 4,2 8,9 12,2 16,9 20,6 80,6" fill="none" stroke="#f78f20" stroke-width="1.6"/></svg>

<article class="quote-card" style="left:145px">
  <div class="avatar" role="img" aria-label="Portrait photo of the client"></div>
  <p class="quote-text">Kielbasa proident laboris, ground round filet mignon andjaeger laborum ham porchetta frankfurter short ribs sirloin andouille. Spare ribs shank dolore beef ribs ground.</p>
  <span class="quote-rule"></span>
  <h4 class="quote-name">Alan R. Whitby</h4>
  <p class="quote-company">Company Inc.</p>
</article>
<article class="quote-card" style="left:458px">
  <div class="avatar" role="img" aria-label="Portrait photo of the client"></div>
  <p class="quote-text">Kielbasa proident laboris, ground round filet mignon andjaeger laborum ham porchetta frankfurter short ribs sirloin andouille. Spare ribs shank dolore beef ribs ground.</p>
  <span class="quote-rule"></span>
  <h4 class="quote-name">Alan R. Whitby</h4>
  <p class="quote-company">Company Inc.</p>
</article>
<article class="quote-card" style="left:770px">
  <div class="avatar" role="img" aria-label="Portrait photo of the client"></div>
  <p class="quote-text">Kielbasa proident laboris, ground round filet mignon andjaeger laborum ham porchetta frankfurter short ribs sirloin andouille. Spare ribs shank dolore beef ribs ground.</p>
  <span class="quote-rule"></span>
  <h4 class="quote-name">Alan R. Whitby</h4>
  <p class="quote-company">Company Inc.</p>
</article>
<div class="dots"><i class="active"></i><i></i><i></i></div>

<footer class="site-footer">
  <div class="footer-brand"><span class="brand-dot"></span><span class="brand-name">Tidewell Energy</span></div>
  <p class="footer-about">Tidewell Energy is a national company that specialises in solar solutions for the commercial market. We also provide solutions for the residential market, bringing our uncompromising quality and service to the home. Tidewell Energy is a national company that specialises in solar solutions for the commercial market.</p>

  <h4 class="footer-head" style="left:597px">LINKS</h4>
  <ul class="footer-links">
    <li>Solutions</li><li>Products</li><li>About</li><li>Contact</li>
  </ul>

  <h4 class="footer-head" style="left:858px">CONTACT</h4>
  <div class="contact-row" style="top:116px">
    <svg width="10" height="13" viewBox="0 0 10 13"><path d="M5 0a5 5 0 0 0-5 5c0 3.5 5 8 5 8s5-4.5 5-8a5 5 0 0 0-5-5zm0 7a2 2 0 1 1 0-4 2 2 0 0 1 0 4z" fill="#fff"/></svg>
    <span style="width:170px">Labore quis ut venison ball tip short ribs eiusmod minim nulla. Irure ipsum pork belly fatback</span>
  </div>
  <div class="contact-row" style="top:178px">
    <svg width="11" height="11" viewBox="0 0 24 24"><path d="M6.6 10.8a15.1 15.1 0 0 0 6.6 6.6l2.2-2.2a1 1 0 0 1 1-.25 11.4 11.4 0 0 0 3.6.57 1 1 0 0 1 1 1V20a1 1 0 0 1-1 1A17 17 0 0 1 3 4a1 1 0 0 1 1-1h3.5a1 1 0 0 1 1 1c0 1.25.2 2.45.57 3.57a1 1 0 0 1-.25 1z" fill="#fff"/></svg>
    <span>1234567890</span>
  </div>
  <div class="contact-row" style="top:206px">
    <svg width="11" height="9" viewBox="0 0 11 9"><rect width="11" height="9" fill="#fff"/><polyline points="0,0 5.5,5 11,0" fill="none" stroke="#0255a3" stroke-width="1.2"/></svg>
    <span>contact@tidewellmail.com</span>
  </div>
</footer>

</body>
</html>
```